Author of female self help book in need of cover that expresses freedom and empowerment

This is the first in a series of female self help books. It is called Her Quiet Compass. The book tells my story of hitting rock bottom, winning the lottery, and discovering what I call my Quiet Compass. The purpose of the book is to help inspire women to break free from the pain of loss including divorce, job loss, or heartbreak. It will help guide a women's journey to finding their courage and motivation to move on in pursuit of happiness and joy. She will gain skills to help build resilience, tap into her inner strength, achieve success in her personal and professional life and finally create a life she loves to live.

Target Market(s)

Women 30-60 yrs, divorced, single mother, widow, working professional

Industry/Entity Type

Life Coaching

Font styles to use
Serif

Colors
fbd4d5
f59296

Requirements
Must have
• Cover must express female freedom and empowerment.
Nice to have
• I would like to see something like a mountain top scene or woman depicted with arms raised high in victory.

```html
<!DOCTYPE html>
<html lang="en">
<head>
<meta charset="utf-8">
<title>Her Quiet Compass — Book Cover</title>
<link rel="stylesheet" href="https://fonts.googleapis.com/css2?family=Cinzel:wght@400;500&display=swap">
<style>
  :root {
    --page-bg: #f3eee6;
    --night: #15142e;
    --dusk-violet: #2f2a5c;
    --sky-blue: #2f6797;
    --horizon-violet: #3a2c55;
    --horizon-rose: #8a5a78;
    --ground: #0f0f14;
    --blush: #fbd4d5;
    --rose: #f59296;
    --rose-soft: #f4a9ac;
    --sky-light: #9fd0ee;
    --text-light: #f4f1f6;
  }

  * { box-sizing: border-box; margin: 0; padding: 0; }

  html, body {
    width: 1200px;
    height: 730px;
    overflow: hidden;
    background: var(--page-bg);
  }

  .stage {
    width: 1200px;
    height: 730px;
    display: flex;
    align-items: center;
    justify-content: center;
  }

  .book-cover {
    position: relative;
    width: 450px;
    height: 690px;
    overflow: hidden;
    background: linear-gradient(
      to bottom,
      var(--night) 0%,
      var(--dusk-violet) 18%,
      var(--sky-blue) 42%,
      var(--horizon-violet) 62%,
      var(--horizon-rose) 72%,
      var(--ground) 80%,
      var(--ground) 100%
    );
    box-shadow: 0 10px 30px rgba(0, 0, 0, 0.18);
  }

  .cover-heading {
    position: absolute;
    top: 46px;
    left: 0;
    right: 0;
    text-align: center;
    font-family: "Cinzel", serif;
  }

  .title-lead {
    display: block;
    font-size: 28px;
    font-weight: 400;
    letter-spacing: 0.02em;
    color: var(--text-light);
    line-height: 1;
  }

  .title-main {
    display: block;
    margin-top: 8px;
    font-size: 60px;
    font-weight: 400;
    letter-spacing: 0.01em;
    color: var(--rose);
    line-height: 1;
  }

  .byline {
    display: block;
    margin-top: 18px;
    font-size: 17px;
    font-weight: 400;
    letter-spacing: 0.03em;
    color: var(--text-light);
  }

  .cover-art {
    position: absolute;
    left: 58px;
    top: 262px;
    width: 340px;
    height: 428px;
    border-radius: 170px 170px 0 0;
    background: radial-gradient(
      ellipse 45% 55% at 50% 55%,
      var(--sky-light) 0%,
      var(--sky-light) 40%,
      var(--rose-soft) 70%,
      var(--blush) 100%
    );
  }
</style>
</head>
<body>
  <main class="stage">
    <section class="book-cover">
      <h1 class="cover-heading">
        <span class="title-lead">Her Quiet</span>
        <span class="title-main">COMPASS</span>
        <span class="byline">By (Author’s Name)</span>
      </h1>
      <div class="cover-art" role="img" aria-label="Illustration: pink silhouette of a woman's head in profile, inside it a woman standing with arms raised in victory against a sunrise sky with birds"></div>
    </section>
  </main>
</body>
</html>
```